Paw Summit Co business card

I need a business card design for a dog training company in Toronto called Paw Summit Co. My training is unique, outdoor training that helps people create a better bond with their dog through communication and understanding their dog's true nature. I do not use treats - but communication and praise for the dog.

I help people create a better life for them and their dog. From puppy training right through to seniors, I offer both group classes called Curbside Poise Course as well as in-home private sessions.

I believe that having a dog is a lifestyle, so I encourage clients to incorporate their dog into their active life. Outdoor activities such as hiking, mental stimulation, proper care and healthy food for their dog are all keys to a healthy and happy dog.

I would like a fresh and modern look that works with my logo. I would like to convey fun, confidence and happiness.

My services are premium services. I am a Certified Dog Trainer, and offer value for money, but my prices are higher than other trainers.
Updates

Thank you to everyone who submitted designs! I'm so impressed with the level of creativity and the options that you all have given me. It will be a difficult choice for sure. As this was my first experience with Art Huddle - it has been a great one.

maren.

Industry/Entity Type

Communication

Requirements
Must have
• Maren Quill, CTE
Certified Trainer Educator
maren@pawsummitco.ca
555-318-0472
pawsummitco.ca

Prefer a double sided card.
Must have Paw Summit Co logo. File attached. I do have a stroke logo for a dark background as well.

Must only use the fonts and colours as outlined in my brand guidelines, which are attached.
Should not have
• no cheesy pet images
do not use the tongue as an element outside of the logo
minimize the use of pink - can be used as an accent colour but should not be a main colour

```html
<!DOCTYPE html>
<html lang="en">
<head>
<meta charset="utf-8">
<title>Paw Summit Co — Business Card</title>
<link rel="stylesheet" href="https://fonts.googleapis.com/css2?family=Questrial&display=swap">
<style>
  :root {
    --page: #e9e6e1;
    --green: #9fc251;
    --green-dark: #86a83c;
    --blue: #1a9bd2;
    --ink: #333538;
    --white: #ffffff;
    --paper-grey: #eceded;
    --line-grey: #d4d6d8;
  }
  * { box-sizing: border-box; margin: 0; padding: 0; }
  html, body {
    width: 1200px; height: 923px; overflow: hidden;
    background: var(--page);
    font-family: "Questrial", "Century Gothic", sans-serif;
  }
  .sheet {
    width: 1200px; height: 923px;
    display: flex; flex-direction: column; align-items: center; justify-content: center;
    gap: 56px;
  }
  .card {
    position: relative;
    width: 640px; height: 366px;
    border-radius: 22px;
    overflow: hidden;
    box-shadow: 0 6px 18px rgba(0,0,0,.18);
  }

  /* Front */
  .card--front { background: var(--green); }
  .front__stripe {
    position: absolute; top: 0; bottom: 0; left: 488px; width: 40px;
    background: var(--blue);
    display: flex; align-items: center; justify-content: center;
  }
  .front__url {
    transform: rotate(-90deg);
    white-space: nowrap;
    color: var(--white);
    font-size: 15px; letter-spacing: 3px;
  }
  .brand {
    position: absolute;
    display: flex; align-items: center; gap: 12px;
    color: var(--ink);
    font-size: 38px; line-height: 1;
    white-space: nowrap;
  }
  .brand__dot {
    flex: none;
    width: 22px; height: 22px; border-radius: 50%;
    background: var(--white);
  }
  .card--front .brand { left: 110px; top: 164px; }

  /* Back */
  .card--back { background: var(--green); }
  .back__panel { position: absolute; inset: 0; }
  .card--back .brand {
    left: 22px; top: 50%; transform: translateY(-50%);
    font-size: 23px; gap: 9px;
  }
  .card--back .brand__dot { width: 16px; height: 16px; }
  .back__details {
    position: absolute; left: 300px; right: 34px; top: 34px; bottom: 30px;
  }
  .back__name {
    color: var(--green); font-size: 30px; letter-spacing: .5px; font-weight: 400;
  }
  .back__role { color: var(--ink); font-size: 15px; margin-top: 6px; }
  .back__role .back__cred { color: var(--ink); margin-left: 6px; }
  .back__contact {
    position: absolute; right: 0; bottom: 0;
    text-align: right; color: var(--ink); font-size: 14px; line-height: 1.55;
  }
  .back__web {
    color: var(--blue); font-size: 17px; letter-spacing: 2px; margin-top: 4px;
  }
</style>
</head>
<body>
<main class="sheet">

  <section class="card card--front" aria-label="Card front">
    <div class="brand"><span class="brand__dot"></span><span class="brand__name">Paw Summit Co</span></div>
    <div class="front__stripe"><span class="front__url">www.pawsummitco.ca</span></div>
  </section>

  <section class="card card--back" aria-label="Card back">
    <svg class="back__panel" viewBox="0 0 640 366" preserveAspectRatio="none" aria-hidden="true">
      <path d="M262 0 Q 208 183 262 366 L 640 366 L 640 0 Z" fill="var(--line-grey)"/>
      <path d="M270 0 Q 216 183 270 366 L 640 366 L 640 0 Z" fill="none" stroke="var(--blue)" stroke-width="3"/>
      <path d="M280 0 Q 228 183 280 366 L 640 366 L 640 0 Z" fill="var(--white)"/>
      <path d="M292 0 Q 244 183 292 366" fill="none" stroke="var(--paper-grey)" stroke-width="6"/>
    </svg>
    <div class="brand"><span class="brand__dot"></span><span class="brand__name">Paw Summit Co</span></div>
    <div class="back__details">
      <h1 class="back__name">Maren Quill</h1>
      <p class="back__role">Certified Trainer Educator <span class="back__cred">CTE</span></p>
      <div class="back__contact">
        <p>P: 555-318-0472</p>
        <p>E: maren@pawsummitco.ca</p>
        <p>#1321, Your Street, Your Location</p>
        <p>Your Town, Your Country</p>
        <p class="back__web">www.pawsummitco.ca</p>
      </div>
    </div>
  </section>

</main>
</body>
</html>
```